Design Circlebook and CareerLink design for existing company

We have an existing website. We want a modern interactive Circlebook and CareerLink design. Our website is www.CoverLantern.com

Target Market(s)

People aged 30-50. Family oriented

Industry/Entity Type

Life insurance

Font styles to use
Other font styles liked:
• Rubik

Colors
0054AA
0677BA
7BADD7
CADEEF
E8F1F8
00AB8E
00BBA5
67D7C9
C6EFE9
E9F9F6
59FF00
82FF00
B8FF75
E3FFCB
F4FFEA

Requirements
Must have
• It must be modern
Nice to have
• Same color scheme as website
Should not have
• Colors that deviate from our website

```html
<!DOCTYPE html>
<html lang="en">
<head>
<meta charset="utf-8">
<title>Life Insurance Online – Social Cover Presentation</title>
<link href="https://fonts.googleapis.com/css2?family=Rubik:wght@400;500;600&family=Noto+Serif:wght@400&family=Noto+Sans:wght@400&family=Source+Sans+3:wght@400;600&display=swap" rel="stylesheet">
<style>
  :root{
    --brand-blue:#0563AF;
    --brand-green:#8DC63F;
    --check:#7DC783;
    --white:#FFFFFF;
    --stage:#E6E6E6;
    --mock-frame:#E9E9E9;
    --mock-bar:#CFCFCF;
    --ui-blue:#2F80ED;
    --feed-bg:#F3F2EF;
    --ln-blue:#0A66C2;
    --ln-green:#057642;
    --ink:#222222;
    --muted:#666666;
    --soft:#8A8A8A;
    --alert:#D11124;
    --premium:#915907;
  }
  *{box-sizing:border-box;margin:0;padding:0}
  html,body{width:712px;height:1200px;overflow:hidden}
  body{position:relative;background:var(--stage);font-family:"Source Sans 3",sans-serif;color:var(--ink)}
  .abs{position:absolute}

  /* shared cover art */
  .art-head{font-family:"Rubik",sans-serif;font-weight:600;fill:var(--white)}
  .art-list{font-family:"Noto Serif",serif;fill:var(--white)}
  .art-blue{fill:var(--brand-blue)}
  .art-green{fill:var(--brand-green)}
  .art-white{fill:var(--white)}
  .cover-svg{position:absolute;display:block}

  .section-title{position:absolute;left:0;width:100%;text-align:center;font-family:"Noto Sans",sans-serif;font-size:17px;letter-spacing:.4px}
  .section-title--dark{color:var(--ink)}
  .section-title--light{color:#F4F4F4}

  /* desktop & mobile frames */
  .frame{position:absolute;background:var(--mock-frame);border-radius:6px;box-shadow:0 3px 10px rgba(0,0,0,.12);overflow:hidden}
  .bar{position:absolute;background:var(--mock-bar);border-radius:6px}
  .bar--blue{background:var(--ui-blue)}
  .dot{position:absolute;border-radius:50%}
  .ui-line{position:absolute;height:1px;background:#D6D6D6}
  .brand-mark{position:absolute;border-radius:50%;background:var(--ui-blue)}
  .avatar{position:absolute;border-radius:50%;background:#EFEFEF;display:flex;align-items:center;justify-content:center;font-family:"Rubik",sans-serif;color:var(--brand-blue)}

  /* career network page */
  .ln-top{position:absolute;left:0;top:395px;width:712px;height:29px;background:var(--white)}
  .ln-feed{position:absolute;left:0;top:424px;width:712px;height:261px;background:var(--feed-bg);overflow:hidden}
  .ln-mark{position:absolute;left:35px;top:5px;width:19px;height:19px;background:var(--ln-blue);border-radius:2px}
  .ln-search{position:absolute;left:59px;top:6px;width:159px;height:18px;background:#EEF3F8;border-radius:2px;font-size:8px;color:var(--muted);padding:4px 0 0 22px}
  .ln-search svg{position:absolute;left:9px;top:4px}
  .nav-item{position:absolute;top:4px;width:46px;margin-left:-23px;text-align:center;font-size:7px;color:var(--muted)}
  .nav-item svg{display:block;margin:0 auto 2px}
  .badge{position:absolute;top:-1px;left:27px;min-width:9px;height:9px;padding:0 2px;border-radius:5px;background:var(--alert);color:var(--white);font-size:6px;line-height:9px;font-weight:600}
  .nav-divider{position:absolute;left:574px;top:2px;width:1px;height:25px;background:#E0E0E0}
  .premium{position:absolute;left:624px;top:6px;width:52px;text-align:center;font-size:7px;line-height:10px;color:var(--premium)}

  .card{position:absolute;background:var(--white);border-radius:5px;box-shadow:0 0 0 1px rgba(0,0,0,.06)}
  .company-logo{position:absolute;left:18px;top:49px;width:55px;height:54px;background:var(--white);border:2px solid #EDEDED;display:flex;align-items:center;justify-content:center;font-family:"Rubik",sans-serif;font-size:8px;color:var(--brand-blue)}
  .company-name{position:absolute;left:13px;top:113px;font-size:14px;font-weight:600}
  .company-tag{position:absolute;left:13px;top:130px;font-size:8.5px}
  .company-meta{position:absolute;left:13px;top:142px;font-size:7.5px;color:var(--soft)}
  .company-staff{position:absolute;left:13px;top:158px;font-size:8.5px;color:var(--muted)}
  .btn{position:absolute;top:180px;height:18px;border-radius:9px;font-size:9px;font-weight:600;display:flex;align-items:center;justify-content:center;gap:3px}
  .btn--primary{left:13px;width:77px;background:var(--ln-blue);color:var(--white)}
  .btn--outline{left:95px;width:83px;border:1px solid var(--ln-blue);color:var(--ln-blue)}
  .btn--quiet{left:184px;width:39px;border:1px solid var(--soft);color:var(--muted);font-weight:400}
  .card-divider{position:absolute;left:0;top:208px;width:100%;height:1px;background:#E6E6E6}
  .tabs{position:absolute;left:11px;top:215px;display:flex;gap:0;font-size:9px;color:var(--muted)}
  .tabs span{margin-right:18px}
  .tabs .is-active{color:var(--ln-green);font-weight:600}
  .tab-underline{position:absolute;left:1px;top:234px;width:45px;height:2px;background:var(--ln-green)}

  .ad-label{position:absolute;right:12px;top:8px;font-size:7px;color:var(--muted)}
  .ad-copy{position:absolute;left:0;width:100%;text-align:center;color:var(--muted)}
  .ad-brand{position:absolute;left:72px;top:41px;width:40px;height:40px;background:linear-gradient(135deg,#1FA24A,#8CD64A 55%,#0E7C3A)}
  .btn--follow{left:69px;top:117px;width:45px;height:17px;border:1px solid var(--ln-blue);color:var(--ln-blue)}
  .side-title{position:absolute;left:9px;top:10px;font-size:11px}
  .side-logo{position:absolute;left:9px;top:47px;width:26px;height:14px;border-radius:7px;border:2px solid #5AA9E6}
  .side-name{position:absolute;left:45px;top:43px;font-size:9px}
  .side-meta{position:absolute;left:45px;font-size:6.5px;color:var(--soft)}

  /* final cover showcase */
  .showcase{position:absolute;left:0;top:685px;width:712px;height:515px;background:linear-gradient(135deg,#3A3A3A 0%,#7E7E7E 40%,#A8A8A8 70%,#C9C9C9 100%)}
  .cover-shadow{box-shadow:0 6px 12px rgba(0,0,0,.35)}
</style>
</head>
<body>

<svg width="0" height="0" class="abs" aria-hidden="true">
  <defs>
    <linearGradient id="photo-tones" x1="0" y1="0" x2="1" y2="0">
      <stop offset="0" stop-color="#C9B2A2"/>
      <stop offset=".45" stop-color="#8E6652"/>
      <stop offset=".8" stop-color="#A88A76"/>
      <stop offset="1" stop-color="#E6DFD8"/>
    </linearGradient>
    <symbol id="tick" viewBox="0 0 10 10">
      <circle cx="5" cy="5" r="4.2" fill="none" stroke="var(--check)" stroke-width=".9"/>
      <path d="M3 5.2L4.4 6.5L7 3.8" fill="none" stroke="var(--check)" stroke-width=".9"/>
    </symbol>
    <g id="fb-art">
      <rect role="img" aria-label="Photo of a smiling father hugging his young daughter" width="676" height="296" fill="url(#photo-tones)"/>
      <path class="art-blue" d="M0 0H292C250 60 250 130 300 180C335 215 330 260 318 296H0Z"/>
      <path class="art-green" d="M292 0H302C262 60 262 130 312 180C348 215 346 260 334 296H318C330 260 335 215 300 180C250 130 250 60 292 0Z"/>
      <text class="art-head" x="84" y="100" font-size="80">Life</text>
      <text class="art-head" x="86" y="132" font-size="28">Insurance</text>
      <rect class="art-green" x="87" y="142" width="140" height="26" rx="13"/>
      <text class="art-head" x="100" y="163" font-size="21" letter-spacing=".5">ONLINE</text>
      <rect class="art-white" x="200" y="145" width="22" height="20" rx="4"/>
      <path d="M205 155H216M212 150.5L216.5 155L212 159.5" fill="none" stroke="var(--brand-green)" stroke-width="2.2" stroke-linecap="round" stroke-linejoin="round"/>
      <use href="#tick" x="88" y="186" width="9" height="9"/>
      <text class="art-list" x="103" y="195" font-size="12">Purchase</text>
      <text class="art-list" x="103" y="211" font-size="12">Life Insurance Online</text>
      <use href="#tick" x="88" y="221" width="9" height="9"/>
      <text class="art-list" x="103" y="230" font-size="12">Quote Yourself</text>
      <use href="#tick" x="88" y="242" width="9" height="9"/>
      <text class="art-list" x="103" y="251" font-size="12">Apply in minutes</text>
    </g>
    <g id="li-art">
      <rect role="img" aria-label="Photo of a smiling father and daughter side by side" width="1306" height="326" fill="url(#photo-tones)"/>
      <path class="art-blue" d="M0 0H580C530 60 535 130 590 190C640 245 640 290 605 326H0Z"/>
      <path class="art-green" d="M580 0H598C548 60 553 130 608 190C658 245 658 290 623 326H605C640 290 640 245 590 190C535 130 530 60 580 0Z"/>
      <text class="art-head" x="69" y="112" font-size="66">Life Insurance</text>
      <rect class="art-green" x="254" y="128" width="184" height="36" rx="18"/>
      <text class="art-head" x="270" y="157" font-size="29" letter-spacing=".6">ONLINE</text>
      <rect class="art-white" x="401" y="131" width="32" height="30" rx="6"/>
      <path d="M409 146H425M419 139.5L425.5 146L419 152.5" fill="none" stroke="var(--brand-green)" stroke-width="3" stroke-linecap="round" stroke-linejoin="round"/>
      <use href="#tick" x="263" y="182" width="14" height="14"/>
      <text class="art-list" x="285" y="196" font-size="19">Purchase Life Insurance Online</text>
      <use href="#tick" x="263" y="208" width="14" height="14"/>
      <text class="art-list" x="285" y="222" font-size="19">Quote Yourself</text>
      <use href="#tick" x="263" y="234" width="14" height="14"/>
      <text class="art-list" x="285" y="248" font-size="19">Apply in minutes</text>
    </g>
  </defs>
</svg>

<!-- Circlebook mockups -->
<h2 class="section-title section-title--dark" style="top:27px">CIRCLEBOOK COVER MOCKUP</h2>

<section class="frame" style="left:65px;top:64px;width:397px;height:271px" aria-label="Desktop profile page">
  <span class="dot" style="left:12px;top:11px;width:7px;height:7px;background:#F25A54"></span>
  <span class="dot" style="left:24px;top:11px;width:7px;height:7px;background:#F6BE2F"></span>
  <span class="dot" style="left:35px;top:11px;width:7px;height:7px;background:#2DC53F"></span>
  <span class="ui-line" style="left:0;top:27px;width:100%"></span>
  <span class="brand-mark" style="left:12px;top:35px;width:17px;height:17px"></span>
  <span class="bar" style="left:34px;top:36px;width:106px;height:17px;border-radius:9px"></span>
  <span class="dot" style="left:247px;top:38px;width:12px;height:12px;background:var(--mock-bar)"></span>
  <span class="bar" style="left:264px;top:43px;width:26px;height:3px"></span>
  <span class="dot" style="left:302px;top:35px;width:17px;height:17px;background:var(--mock-bar)"></span>
  <span class="dot" style="left:324px;top:35px;width:17px;height:17px;background:var(--mock-bar)"></span>
  <span class="dot" style="left:346px;top:35px;width:17px;height:17px;background:var(--mock-bar)"></span>
  <span class="dot" style="left:367px;top:35px;width:17px;height:17px;background:var(--mock-bar)"></span>
  <span class="dot" style="left:358px;top:36px;width:5px;height:5px;background:var(--alert)"></span>

  <svg class="cover-svg" style="left:30px;top:66px;border-radius:4px" width="337" height="128" viewBox="0 0 676 296" preserveAspectRatio="xMidYMid slice"><use href="#fb-art"/></svg>
  <div class="avatar" style="left:42px;top:187px;width:48px;height:48px;font-size:7px">CoverLantern</div>

  <span class="bar" style="left:99px;top:204px;width:77px;height:8px"></span>
  <span class="bar" style="left:99px;top:218px;width:58px;height:5px"></span>
  <span class="bar bar--blue" style="left:244px;top:217px;width:111px;height:14px;border-radius:2px"></span>
  <span class="ui-line" style="left:42px;top:241px;width:313px"></span>
  <span class="bar bar--blue" style="left:45px;top:249px;width:20px;height:8px"></span>
  <span class="bar" style="left:71px;top:249px;width:22px;height:8px"></span>
  <span class="bar" style="left:99px;top:249px;width:16px;height:8px"></span>
  <span class="bar" style="left:121px;top:249px;width:19px;height:8px"></span>
  <span class="dot" style="left:143px;top:251px;width:4px;height:4px;background:var(--mock-bar)"></span>
  <span class="bar bar--blue" style="left:42px;top:261px;width:26px;height:1px;border-radius:0"></span>
  <span class="bar" style="left:221px;top:246px;width:42px;height:14px;border-radius:2px"></span>
  <span class="bar" style="left:268px;top:246px;width:42px;height:14px;border-radius:2px"></span>
  <span class="bar" style="left:314px;top:246px;width:18px;height:14px;border-radius:2px"></span>
  <span class="bar" style="left:337px;top:246px;width:18px;height:14px;border-radius:2px"></span>
</section>

<section class="frame" style="left:494px;top:64px;width:152px;height:271px" aria-label="Mobile profile page">
  <span class="brand-mark" style="left:6px;top:6px;width:17px;height:17px"></span>
  <span class="bar" style="left:27px;top:6px;width:120px;height:17px;border-radius:9px"></span>
  <svg class="cover-svg" style="left:0;top:30px" width="152" height="85" viewBox="0 0 676 296" preserveAspectRatio="xMidYMid slice"><use href="#fb-art"/></svg>
  <div class="avatar" style="left:4px;top:120px;width:24px;height:24px;font-size:3.5px">CoverLantern</div>
  <span class="bar" style="left:34px;top:129px;width:43px;height:4px"></span>
  <span class="bar" style="left:34px;top:135px;width:33px;height:2px"></span>
  <span class="dot" style="left:129px;top:123px;width:18px;height:18px;background:#DEDEDE"></span>
  <span class="bar bar--blue" style="left:6px;top:151px;width:93px;height:13px;border-radius:2px"></span>
  <span class="bar" style="left:104px;top:151px;width:19px;height:13px;border-radius:2px"></span>
  <span class="bar" style="left:128px;top:151px;width:19px;height:13px;border-radius:2px"></span>
  <span class="bar" style="left:9px;top:171px;width:32px;height:3px"></span>
  <span class="bar bar--blue" style="left:6px;top:188px;width:17px;height:8px"></span>
  <span class="bar" style="left:29px;top:188px;width:22px;height:8px"></span>
  <span class="bar" style="left:57px;top:188px;width:16px;height:8px"></span>
  <span class="bar" style="left:79px;top:188px;width:19px;height:8px"></span>
  <span class="bar" style="left:104px;top:188px;width:19px;height:8px"></span>
  <span class="bar" style="left:128px;top:188px;width:19px;height:8px"></span>
  <span class="bar bar--blue" style="left:3px;top:200px;width:23px;height:1px;border-radius:0"></span>
  <span class="bar" style="left:6px;top:223px;width:28px;height:4px"></span>
  <span class="bar" style="left:88px;top:223px;width:59px;height:4px"></span>
  <span class="bar" style="left:6px;top:235px;width:122px;height:3px"></span>
  <span class="bar" style="left:6px;top:244px;width:141px;height:3px"></span>
  <span class="bar" style="left:6px;top:253px;width:87px;height:3px"></span>
</section>

<!-- CareerLink mockup -->
<h2 class="section-title section-title--dark" style="top:363px">CAREERLINK COVER MOCKUP</h2>

<header class="ln-top" aria-label="CareerLink navigation">
  <span class="ln-mark"></span>
  <div class="ln-search">
    <svg width="9" height="9" viewBox="0 0 10 10"><circle cx="4" cy="4" r="3" fill="none" stroke="var(--ink)" stroke-width="1.4"/><path d="M6.3 6.3L9 9" stroke="var(--ink)" stroke-width="1.4"/></svg>Search
  </div>
  <div class="nav-item" style="left:323px"><svg width="12" height="11" viewBox="0 0 12 11"><path d="M6 0L12 5V11H0V5Z" fill="var(--muted)"/></svg>Home<span class="badge" style="min-width:6px;width:6px;height:6px;padding:0;left:30px"></span></div>
  <div class="nav-item" style="left:369px"><svg width="12" height="11" viewBox="0 0 12 11"><circle cx="3.5" cy="2.5" r="2.3" fill="var(--muted)"/><circle cx="9" cy="3.5" r="2" fill="var(--muted)"/><rect x="0.5" y="5.5" width="6" height="5.5" rx="1.5" fill="var(--muted)"/><rect x="7" y="6.5" width="4.5" height="4.5" rx="1.2" fill="var(--muted)"/></svg>My Network</div>
  <div class="nav-item" style="left:415px"><svg width="12" height="11" viewBox="0 0 12 11"><rect x="4" y="0.5" width="4" height="3" fill="none" stroke="var(--muted)"/><rect x="0" y="3" width="12" height="8" rx="1.5" fill="var(--muted)"/></svg>Jobs</div>
  <div class="nav-item" style="left:460px"><svg width="12" height="11" viewBox="0 0 12 11"><path d="M1 0H11A1 1 0 0 1 12 1V7A1 1 0 0 1 11 8H4L1 11V8A1 1 0 0 1 0 7V1A1 1 0 0 1 1 0Z" fill="var(--muted)"/></svg>Messaging<span class="badge">2</span></div>
  <div class="nav-item" style="left:506px"><svg width="12" height="11" viewBox="0 0 12 11"><path d="M6 0C3.5 0 2.5 2 2.5 4V7L1 9H11L9.5 7V4C9.5 2 8.5 0 6 0Z M4.5 9.5H7.5A1.5 1.5 0 0 1 4.5 9.5Z" fill="var(--muted)"/></svg>Notifications<span class="badge">14</span></div>
  <div class="nav-item" style="left:551px"><svg width="12" height="11" viewBox="0 0 12 11"><circle cx="6" cy="5.5" r="5.5" fill="#C9CFD6"/><circle cx="6" cy="4.2" r="2" fill="#8C96A3"/></svg>Me ▾</div>
  <span class="nav-divider"></span>
  <div class="nav-item" style="left:597px"><svg width="12" height="11" viewBox="0 0 12 11"><g fill="var(--muted)"><rect x="1" y="0" width="2" height="2"/><rect x="5" y="0" width="2" height="2"/><rect x="9" y="0" width="2" height="2"/><rect x="1" y="4.5" width="2" height="2"/><rect x="5" y="4.5" width="2" height="2"/><rect x="9" y="4.5" width="2" height="2"/><rect x="1" y="9" width="2" height="2"/><rect x="5" y="9" width="2" height="2"/><rect x="9" y="9" width="2" height="2"/></g></svg>Work ▾</div>
  <div class="premium">Try Premium for free</div>
</header>

<main class="ln-feed">
  <article class="card" style="left:35px;top:14px;width:445px;height:236px;overflow:hidden" aria-label="Company page">
    <svg class="cover-svg" style="left:0;top:0" width="445" height="76" viewBox="0 0 1306 326" preserveAspectRatio="xMidYMid slice"><use href="#li-art"/></svg>
    <div class="company-logo">CoverLantern</div>
    <div class="company-name">CoverLantern</div>
    <div class="company-tag">Online Life Insurance from America's Top Carriers</div>
    <div class="company-meta">Insurance · Willow Creek, FL · 72 followers</div>
    <div class="company-staff">See 1 employee on CareerLink</div>
    <div class="btn btn--primary">+ Follow</div>
    <div class="btn btn--outline">Visit website
      <svg width="8" height="8" viewBox="0 0 10 10"><path d="M4 1H1V9H9V6M6 1H9V4M9 1L4.5 5.5" fill="none" stroke="var(--ln-blue)" stroke-width="1.4"/></svg>
    </div>
    <div class="btn btn--quiet">More</div>
    <span class="card-divider"></span>
    <nav class="tabs"><span class="is-active">Home</span><span>About</span><span>Posts</span><span>Jobs</span><span>People</span></nav>
    <span class="tab-underline"></span>
  </article>
  <span class="card" style="left:35px;top:259px;width:445px;height:10px"></span>

  <aside class="card" style="left:494px;top:14px;width:183px;height:147px" aria-label="Sponsored suggestion">
    <span class="ad-label">Ad &nbsp;•••</span>
    <p class="ad-copy" style="top:24px;font-size:6.5px">stay informed on industry news and trends</p>
    <span class="ad-brand"></span>
    <p class="ad-copy" style="top:86px;font-size:8.5px;line-height:11px">grow your career by following<br>Petrova</p>
    <div class="btn btn--follow">Follow</div>
  </aside>

  <aside class="card" style="left:494px;top:170px;width:183px;height:100px" aria-label="Pages people also viewed">
    <div class="side-title">Pages people also viewed</div>
    <span class="side-logo"></span>
    <div class="side-name">AssureDoc</div>
    <div class="side-meta" style="top:57px">Insurance</div>
    <div class="side-meta" style="top:68px">651 followers</div>
    <span class="abs" style="left:46px;top:85px;width:54px;height:18px;border:1px solid var(--muted);border-radius:9px"></span>
  </aside>
</main>

<!-- Final covers -->
<section class="showcase" aria-label="Final covers">
  <h2 class="section-title section-title--light" style="top:36px">CIRCLEBOOK COVER</h2>
  <svg class="cover-svg cover-shadow" style="left:194px;top:78px" width="324" height="142" viewBox="0 0 676 296" preserveAspectRatio="xMidYMid slice" aria-label="Circlebook cover"><use href="#fb-art"/></svg>
  <h2 class="section-title section-title--light" style="top:255px;left:-7px">CAREERLINK COVER</h2>
  <svg class="cover-svg cover-shadow" style="left:43px;top:288px" width="627" height="157" viewBox="0 0 1306 326" preserveAspectRatio="xMidYMid slice" aria-label="CareerLink cover"><use href="#li-art"/></svg>
</section>

</body>
</html>
```